BRIM Exterior Coatings

double sided. the front i want the name of the business each word on a new line with the BRIM being bigger. id like teal, black and white colors. the back i want my contact info. Flat, no gloss. Something professional and I want to feel the letters bump put of the card. if possible maybe a paint sprayer in corner. not a car paint spray. (no tank on top of gun)
no vehicle paint sprayers. that means no tank on top of the gun. doesn't have to have a sprayer. black/dark background on the front. white back ground on back with info

```html
<!DOCTYPE html>
<html lang="en">
<head>
<meta charset="utf-8">
<title>BRIM Exterior Coatings – Business Card</title>
<link href="https://fonts.googleapis.com/css2?family=Krona+One&family=Arimo:wght@400&display=swap" rel="stylesheet">
<style>
  :root {
    --stage: #2a2a2a;
    --card-dark: #0d0d0d;
    --card-light: #f7f7f7;
    --ink: #262626;
    --silver: #cfcfcf;
    --teal: #1b9a98;
  }
  * { box-sizing: border-box; margin: 0; padding: 0; }
  html, body { width: 1200px; height: 900px; overflow: hidden; }
  body {
    background: var(--stage);
    font-family: "Arimo", Arial, sans-serif;
    position: relative;
  }
  .card {
    position: absolute;
    width: 520px;
    height: 298px;
    border-radius: 22px;
  }
  .card--front { left: 620px; top: 130px; background: var(--card-dark); }
  .card--back  { left: 60px;  top: 470px; background: var(--card-light); }

  .wordmark {
    position: absolute;
    font-family: "Krona One", sans-serif;
    line-height: 1.05;
    letter-spacing: 0.01em;
    display: flex;
    align-items: flex-start;
    gap: 14px;
  }
  .wordmark__square { width: 14px; height: 14px; background: var(--teal); margin-top: 12px; }
  .wordmark__brim { display: block; font-size: 64px; }
  .wordmark__word { display: block; font-size: 24px; }

  .card--front .wordmark { left: 120px; top: 62px; color: var(--silver); }
  .card--back  .wordmark { left: 268px; top: 28px; color: var(--ink); }
  .card--back  .wordmark__brim { font-size: 44px; }
  .card--back  .wordmark__word { font-size: 17px; }
  .card--back  .wordmark__square { width: 10px; height: 10px; margin-top: 9px; }

  .divider {
    position: absolute;
    left: 250px; right: 28px; top: 178px;
    height: 1px; background: var(--teal);
  }
  .address {
    position: absolute;
    right: 30px; top: 190px;
    text-align: right;
    font-size: 14px; line-height: 1.35;
    color: var(--ink);
  }
  .person { position: absolute; left: 30px; top: 160px; }
  .person__name {
    font-family: "Krona One", sans-serif;
    font-size: 19px; color: var(--teal);
  }
  .person__role { font-size: 14px; color: var(--ink); margin-top: 2px; }
  .contacts { list-style: none; margin-top: 10px; }
  .contacts li {
    display: flex; align-items: center; gap: 7px;
    font-size: 14px; line-height: 1.4; color: var(--ink);
  }
  .contacts svg { width: 13px; height: 13px; fill: var(--teal); flex: none; }
  .contacts .accent { color: var(--teal); }
</style>
</head>
<body>
  <section class="card card--front" aria-label="Card front">
    <div class="wordmark">
      <span class="wordmark__square"></span>
      <div>
        <span class="wordmark__brim">BRIM</span>
        <span class="wordmark__word">EXTERIOR</span>
        <span class="wordmark__word">COATINGS</span>
      </div>
    </div>
  </section>

  <section class="card card--back" aria-label="Card back">
    <div class="wordmark">
      <span class="wordmark__square"></span>
      <div>
        <span class="wordmark__brim">BRIM</span>
        <span class="wordmark__word">EXTERIOR</span>
        <span class="wordmark__word">COATINGS</span>
      </div>
    </div>
    <div class="divider"></div>
    <p class="address">88, Harbor Road Suite 4<br>32207,United States</p>
    <div class="person">
      <p class="person__name">DANA REYES</p>
      <p class="person__role">Managing Director</p>
      <ul class="contacts">
        <li><svg viewBox="0 0 16 16"><path d="M3.5 1.5l2.5 0 1 3.5-1.6 1.1a8 8 0 0 0 4.5 4.5L11 9l3.5 1v2.5A1.5 1.5 0 0 1 13 14 11 11 0 0 1 2 3a1.5 1.5 0 0 1 1.5-1.5z"/></svg>044-555 210 734</li>
        <li><svg viewBox="0 0 16 16"><path d="M1 3h14v10H1z M1.5 3.5L8 9l6.5-5.5" fill="none" stroke="#1b9a98" stroke-width="1.6"/></svg>hello@brimcoatings.com</li>
        <li><svg viewBox="0 0 16 16"><circle cx="8" cy="8" r="6.5" fill="none" stroke="#1b9a98" stroke-width="1.4"/><path d="M1.5 8h13M8 1.5v13M3 4.5h10M3 11.5h10" stroke="#1b9a98" stroke-width="1.1" fill="none"/></svg>www.<span class="accent">brimcoatings</span>.com</li>
      </ul>
    </div>
  </section>
</body>
</html>
```